Alaska Law Firm Needs a Sticker Design

We need a design for stickers to put on already-printed brochures. We mail the brochures to potential clients so they can learn more about accident-induced injuries, insurance claims, legal representation, and our own law firm.

One of our lawyers wrote a book that provides a helpful overview of personal injury claims. We are offering this book for free to anyone who calls and requests it. Therefore, the sticker design should include one of the following phrases, or something very similar:
a) "Still have questions? Call and request our book-- for free!"
b) "Still have questions about auto accident claims? Call and request our book today."
c) "Still have questions about filing a claim? Call and request a free copy of our book."
d) "Still have questions? Call us today to request a free copy of our book, Clear Lanes Ahead."
e) "To learn more about automobile accidents and insurance, call today and request a free copy of our book."

The sticker should be approximately 3"x3" and may be a circle, square, rectangle, or ellipsis. The sticker will be placed on the back of the folder, which is light blue. We would like the sticker to match the color scheme of our website and the folder.

I will upload an image of the book cover as soon as I obtain it.

Industry/Entity Type

Law Firm

Font styles to use
Serif
Sans Serif

Requirements
Should not have
• Bright colors that aren't already used in the folder design. e.g. no bright orange, pink, chartreuse, turquoise, yellow, red.

```html
<!DOCTYPE html>
<html lang="en">
<head>
<meta charset="utf-8">
<title>Right Turns Only – Free Book Sticker</title>
<link rel="stylesheet" href="https://fonts.googleapis.com/css2?family=Rye&family=Crimson+Text:ital,wght@0,400;0,600;1,400&display=swap">
<style>
  :root {
    --page-bg: #ececec;
    --navy: #1f2a6e;
    --royal: #2b3aa6;
    --ink: #1a1a1a;
    --white: #ffffff;
    --sheen: #d9dbe2;
  }
  html, body {
    margin: 0;
    padding: 0;
    width: 1200px;
    height: 1200px;
    overflow: hidden;
    background: var(--page-bg);
  }
  .canvas {
    width: 1200px;
    height: 1200px;
    display: flex;
    align-items: center;
    justify-content: center;
  }
  .sticker {
    width: 860px;
    height: 967px;
  }
  .firm-name {
    font-family: "Crimson Text", Georgia, serif;
    font-weight: 400;
    fill: var(--navy);
    letter-spacing: 1px;
  }
  .headline {
    font-family: "Rye", "Georgia", serif;
    fill: var(--ink);
  }
  .banner-text {
    font-family: "Rye", "Georgia", serif;
    fill: var(--white);
  }
  .offer {
    font-family: "Crimson Text", Georgia, serif;
    font-style: italic;
    fill: var(--ink);
  }
  .offer-free {
    font-family: "Crimson Text", Georgia, serif;
    fill: var(--royal);
  }
</style>
</head>
<body>
<main class="canvas">
  <svg class="sticker" viewBox="0 0 800 900" xmlns="http://www.w3.org/2000/svg" aria-label="Sticker: Still have questions? Call and request our book for free!">
    <defs>
      <linearGradient id="face-fill" x1="0" y1="0" x2="1" y2="1">
        <stop offset="0" stop-color="#ffffff"/>
        <stop offset="0.55" stop-color="#f4f5f8"/>
        <stop offset="1" stop-color="#d6d8df"/>
      </linearGradient>
      <linearGradient id="banner-fill" x1="0" y1="0" x2="0" y2="1">
        <stop offset="0" stop-color="#3444b8"/>
        <stop offset="1" stop-color="#1f2a8a"/>
      </linearGradient>
    </defs>

    <!-- shield body -->
    <path class="shield"
      d="M120 140 Q400 40 680 140 Q760 170 740 280 C720 420 780 520 700 620 C620 720 440 720 400 860 C360 720 180 720 100 620 C20 520 80 420 60 280 Q40 170 120 140 Z"
      fill="url(#face-fill)" stroke="var(--royal)" stroke-width="28" stroke-linejoin="round"/>
    <path class="shield-inner-line"
      d="M130 162 Q400 68 670 162 Q734 186 718 282 C698 420 754 514 682 604 C608 694 440 700 400 818 C360 700 192 694 118 604 C46 514 102 420 82 282 Q66 186 130 162 Z"
      fill="none" stroke="#c7cad4" stroke-width="3"/>

    <!-- firm name -->
    <rect class="firm-mark" x="228" y="150" width="62" height="62" fill="var(--navy)"/>
    <text class="firm-name" x="304" y="178" font-size="38">RIGHT TURNS</text>
    <text class="firm-name" x="304" y="214" font-size="38">ONLY</text>

    <!-- headline -->
    <text class="headline" x="400" y="318" font-size="66" text-anchor="middle">STILL HAVE</text>

    <!-- ribbon banner -->
    <g class="banner">
      <path d="M10 352 L70 352 L70 450 L10 450 L38 401 Z" fill="var(--navy)"/>
      <path d="M790 352 L730 352 L730 450 L790 450 L762 401 Z" fill="var(--navy)"/>
      <rect x="50" y="338" width="700" height="100" fill="url(#banner-fill)"/>
      <text class="banner-text" x="400" y="418" font-size="86" text-anchor="middle">QUESTIONS?</text>
    </g>

    <!-- offer -->
    <text class="offer" x="400" y="530" font-size="50" text-anchor="middle">Call and request our book</text>
    <text class="offer-free" x="400" y="604" font-size="64" text-anchor="middle">FOR FREE!</text>
  </svg>
</main>
</body>
</html>
```